Margarita Company needs Table Tent Design

Ever at a restaurant and see a mouth-watering table side advertisement for a refreshing beverage? We make Margarita Mix. We need to design a Table Tent for display on the tables in Mexican restaurants to encourage restaurant patrons to order more On the Rocks Margaritas. Design is 2 sided - each side is 4.5" (wide) x 6" (tall).

Target Market(s)

Restaurant Patrons that are visiting a restaurant, generally Mexican restaurants.

Industry/Entity Type

Mexican Restaurant

Font styles to use
Serif

Requirements
Must have
• Mouth-watering design.
Nice to have
• Marketing copy that sells more drinks.
Should not have
• Inappropriate language or images that you wouldn't share with a parent. Also, our main goal is to help the restaurants sell more drinks so we do not usually feature our company logo but we like to add our company web address in a subtle manner.

```html
<!DOCTYPE html>
<html lang="en">
<head>
<meta charset="utf-8">
<title>Margaritas Table Tent</title>
<link href="https://fonts.googleapis.com/css2?family=Arvo:wght@700&family=Oswald:wght@500;600&display=swap" rel="stylesheet">
<style>
  :root {
    --orange: #f7941d;
    --amber: #fbb03b;
    --flame: #f15a24;
    --crimson: #c1272d;
    --ink: #050505;
    --strip: #111111;
    --lime: #c9d531;
    --shadow: #7a3b12;
  }
  html, body {
    margin: 0;
    padding: 0;
    width: 878px;
    height: 1200px;
    overflow: hidden;
    background: var(--orange);
  }
  .table-tent {
    display: block;
    width: 878px;
    height: 1200px;
  }
  .brand-title {
    font-family: "Arvo", Georgia, serif;
    font-weight: 700;
    fill: var(--lime);
  }
  .headline {
    font-family: "Oswald", "Arial Narrow", sans-serif;
    font-weight: 600;
    fill: var(--lime);
  }
  .web-address {
    font-family: "Oswald", "Arial Narrow", sans-serif;
    font-weight: 500;
    fill: var(--lime);
    font-size: 26px;
  }
</style>
</head>
<body>
<svg class="table-tent" viewBox="0 0 878 1200" xmlns="http://www.w3.org/2000/svg">
  <defs>
    <radialGradient id="citrus-glow" cx="0.5" cy="0.5" r="0.5">
      <stop offset="0" stop-color="#f7a21d"/>
      <stop offset="0.55" stop-color="#d9700f" stop-opacity="0.75"/>
      <stop offset="1" stop-color="#d9700f" stop-opacity="0"/>
    </radialGradient>
    <radialGradient id="lime-glow" cx="0.5" cy="0.5" r="0.5">
      <stop offset="0" stop-color="#d4ea3a"/>
      <stop offset="0.45" stop-color="#b7d72a"/>
      <stop offset="0.8" stop-color="#7f9a18" stop-opacity="0.7"/>
      <stop offset="1" stop-color="#4a5a0c" stop-opacity="0"/>
    </radialGradient>
    <radialGradient id="rim-glow" cx="0.5" cy="0.5" r="0.5">
      <stop offset="0" stop-color="#f2f6d8" stop-opacity="0.75"/>
      <stop offset="1" stop-color="#e6f0a8" stop-opacity="0"/>
    </radialGradient>
  </defs>

  <g class="backdrop-bands">
    <rect width="878" height="1200" fill="var(--orange)"/>
    <path d="M0 0 H878 V40 Q440 70 0 30 Z" fill="var(--flame)"/>
    <path d="M0 120 Q440 150 878 110 V160 Q440 200 0 165 Z" fill="var(--crimson)"/>
    <path d="M0 240 Q440 270 878 230 V275 Q440 310 0 280 Z" fill="var(--amber)"/>
    <path d="M0 340 Q440 370 878 330 V395 Q440 430 0 400 Z" fill="var(--flame)"/>
    <path d="M0 470 Q440 500 878 460 V500 Q440 535 0 505 Z" fill="var(--crimson)"/>
    <path d="M0 580 Q440 610 878 570 V620 Q440 655 0 625 Z" fill="var(--amber)"/>
    <path d="M0 700 Q440 730 878 690 V760 Q440 795 0 765 Z" fill="var(--crimson)"/>
    <path d="M0 830 Q440 860 878 820 V865 Q440 900 0 870 Z" fill="var(--flame)"/>
    <path d="M0 940 Q440 970 878 930 V980 Q440 1015 0 985 Z" fill="var(--amber)"/>
    <path d="M0 1050 Q440 1080 878 1040 V1090 Q440 1125 0 1095 Z" fill="var(--crimson)"/>
    <path d="M0 1150 Q440 1180 878 1140 V1200 H0 Z" fill="var(--flame)"/>
  </g>

  <g class="poster-panel" transform="rotate(-1.2 448 600)">
    <rect class="panel-shadow" x="66" y="58" width="778" height="1100" fill="var(--shadow)" opacity="0.55"/>
    <rect class="panel-base" x="58" y="50" width="778" height="1100" fill="var(--ink)"/>

    <g class="drink-photo" role="img"
       aria-label="Photo of a splashing lime margarita in a salt-rimmed glass with straws and an orange slice">
      <rect x="66" y="56" width="764" height="1088" fill="var(--ink)"/>
      <ellipse cx="370" cy="460" rx="210" ry="150" fill="url(#citrus-glow)"/>
      <ellipse cx="520" cy="820" rx="360" ry="240" fill="url(#lime-glow)"/>
      <ellipse cx="520" cy="710" rx="330" ry="60" fill="url(#rim-glow)"/>
      <ellipse cx="520" cy="560" rx="200" ry="110" fill="url(#rim-glow)" opacity="0.5"/>
    </g>

    <rect class="title-strip" x="60" y="50" width="172" height="1100" fill="var(--strip)" opacity="0.9"/>

    <text class="brand-title" font-size="150"
          transform="translate(214 1090) rotate(-90)"
          textLength="956" lengthAdjust="spacingAndGlyphs">MARGARITAS</text>

    <text class="headline" x="786" y="190" font-size="100" text-anchor="end"
          textLength="393" lengthAdjust="spacingAndGlyphs">WE BRING THE</text>
    <text class="headline" x="788" y="308" font-size="126" text-anchor="end"
          textLength="535" lengthAdjust="spacingAndGlyphs">PARTY TO YOU!</text>

    <text class="web-address" x="490" y="1108" text-anchor="middle">LIMECREST.COM</text>
  </g>
</svg>
</body>
</html>
```